Business card design needed with logo

My business is called QVM Solutions & it is targeted towards mobile equipment maintenance in the Mining and civil industry. My work involves maintenance planning and maintenance management plus also supply tradespeople on a labour hire basis. We can provide from basic shut-down machine rebuild plans to complete rebuild services supply plans and labour to anywhere in Australia. I would like to use the colours Black, Red and Grey, I had done a desgin as attached but doesn't really explain what we do and gears don't embroider well onto shirts.
Updates

I also wanted to see the something replace the gears maybe just making the QVM lettering look a bit different or put together differently 

Hello I have extended the deadline by a few extra days as I would like to update details on the front of card, details below & can be put which ever way looks good;

Neil Patton
Director
0417562938
QVM@mailbrook.com.au
www.qvmsolutions-demo.com.au

On the back of the card I would like to have the below printed;

Capable of providing, but not limited to, across Australia:
- Contract Maintenance Planning.
- Skilled Mobile Maintenance labour hire.
- New machine build specifications. 
- Plant risk assessments and inspections.
- Shut down and rebuild program planning.
- Preventative maintenance tasks, including build of materials lists, creation and review.

Target Market(s)

Contractors and companies that use small and large earthmoving and mining machines

Industry/Entity Type

Business

Contact Information for Business Card

Trading name is QVM Solutions
My name and title is
Neil Patton Director
0417 562 938
QVM@mailbrook.com.au

Logo Text

QVM

```html
<!DOCTYPE html>
<html lang="en">
<head>
<meta charset="utf-8">
<title>QVM Solutions – Business Card</title>
<link rel="stylesheet" href="https://fonts.googleapis.com/css2?family=Bebas+Neue&family=Open+Sans:wght@400;600&display=swap">
<style>
  :root {
    --bg: #d9dcdf;
    --card-white: #f4f4f4;
    --card-black: #141414;
    --red: #d9261c;
    --red-logo: #c8412f;
    --grey-band: #7a7a7a;
    --grey-mid: #a9a9a9;
    --grey-text: #b8b8b8;
    --ink: #1d1d1d;
    --ink-soft: #555555;
    --icon: #e26a2c;
  }
  * { margin: 0; padding: 0; box-sizing: border-box; }
  html, body {
    width: 1200px; height: 1000px; overflow: hidden;
    background: var(--bg);
    font-family: "Open Sans", Arial, sans-serif;
  }
  .stage {
    position: relative; width: 1200px; height: 1000px;
    display: flex; flex-direction: column; align-items: center; justify-content: center; gap: 70px;
  }
  .card {
    position: relative; width: 630px; height: 360px; overflow: hidden;
    box-shadow: 0 6px 18px rgba(0,0,0,.25);
  }

  /* Front */
  .card--front { background: var(--card-white); }
  .front__side-band {
    position: absolute; left: 0; top: 40px; width: 30px; bottom: 0; background: var(--grey-band);
  }
  .front__corner-block {
    position: absolute; right: 0; top: 0; width: 70px; height: 42px; background: var(--grey-band);
  }
  .front__art-large {
    position: absolute; left: 320px; top: 80px; width: 250px; height: 230px; border-radius: 50%;
    background: radial-gradient(circle, #f4f4f4 0 28%, #d4d4d4 30%, #e2e2e2 70%, rgba(226,226,226,0) 72%);
  }
  .front__art-small {
    position: absolute; left: 60px; top: 55px; width: 130px; height: 130px; border-radius: 50%;
    background: radial-gradient(circle, #f4f4f4 0 30%, #e3e3e3 32%, #ebebeb 68%, rgba(235,235,235,0) 70%);
  }
  .front__red-band {
    position: absolute; left: 330px; right: 0; top: 148px; height: 32px; background: var(--red);
  }
  .front__red-tab {
    position: absolute; left: 0; top: 215px; width: 140px; height: 26px; background: var(--red);
  }
  .holder {
    position: absolute; right: 80px; top: 28px; text-align: right; line-height: 1;
  }
  .holder__name {
    font-family: "Bebas Neue", Impact, sans-serif; font-size: 36px; color: var(--red); letter-spacing: 1px;
  }
  .holder__title {
    font-family: "Bebas Neue", Impact, sans-serif; font-size: 14px; color: var(--ink); letter-spacing: 1px;
  }
  .company {
    position: absolute; left: 150px; top: 192px;
    font-family: "Bebas Neue", Impact, sans-serif; font-size: 54px; font-weight: 400;
    color: var(--ink); letter-spacing: 1px; line-height: 1;
  }
  .contact {
    position: absolute; left: 150px; top: 256px; list-style: none;
    font-size: 13px; color: var(--ink-soft);
  }
  .contact__item { display: flex; align-items: center; gap: 12px; height: 25px; }
  .contact__icon { width: 14px; height: 14px; flex: none; }

  /* Back */
  .card--back { background: var(--card-black); }
  .back__art {
    position: absolute; inset: 0;
    background:
      radial-gradient(circle at 32% 30%, #1f1f1f 0 70px, transparent 72px),
      radial-gradient(circle at 20% 75%, #1b1b1b 0 80px, transparent 82px),
      radial-gradient(circle at 70% 72%, #1c1c1c 0 50px, transparent 52px);
  }
  .brand {
    position: absolute; left: 170px; top: 48px; display: flex; align-items: center; gap: 14px;
  }
  .brand__name {
    font-family: "Open Sans", Arial, sans-serif; font-weight: 600; font-size: 92px; line-height: 1;
    color: var(--red-logo); letter-spacing: -2px;
  }
  .brand__mark {
    width: 80px; height: 80px; border-radius: 50%; background: var(--grey-mid); margin-top: -44px;
  }
  .services {
    position: absolute; left: 70px; right: 40px; top: 178px;
    color: var(--grey-text); font-size: 11.5px; line-height: 18px;
  }
  .services__intro { font-weight: 600; color: #e0e0e0; margin-bottom: 4px; }
  .services__list { list-style: none; }
  .services__item { padding-left: 14px; position: relative; }
  .services__item::before {
    content: ""; position: absolute; left: 0; top: 7px; width: 6px; height: 6px; background: var(--red);
  }
</style>
</head>
<body>
<main class="stage">
  <section class="card card--front" aria-label="Business card front">
    <div class="front__side-band"></div>
    <div class="front__corner-block"></div>
    <div class="front__art-small" role="img" aria-label="Faint gear illustration"></div>
    <div class="front__art-large" role="img" aria-label="Large light grey gear illustration"></div>
    <div class="front__red-band"></div>
    <div class="front__red-tab"></div>
    <div class="holder">
      <p class="holder__name">NEIL PATTON</p>
      <p class="holder__title">DIRECTOR</p>
    </div>
    <h1 class="company">QVM SOLUTIONS</h1>
    <ul class="contact">
      <li class="contact__item">
        <svg class="contact__icon" viewBox="0 0 16 16" aria-hidden="true">
          <circle cx="8" cy="8" r="7" fill="none" stroke="var(--icon)" stroke-width="1.4"/>
          <path d="M5.5 4.5l1.4 1.6-.8 1c.5 1 1.3 1.8 2.3 2.3l1-.8 1.6 1.4-.9 1.2C8 11 5 8 4.3 5.4z" fill="var(--icon)"/>
        </svg>
        <span>0417 562 938</span>
      </li>
      <li class="contact__item">
        <svg class="contact__icon" viewBox="0 0 16 16" aria-hidden="true">
          <rect x="2" y="4" width="12" height="9" fill="none" stroke="var(--icon)" stroke-width="1.4"/>
          <path d="M2 4l6 5 6-5" fill="none" stroke="var(--icon)" stroke-width="1.4"/>
        </svg>
        <span>QVM@mailbrook.com.au</span>
      </li>
      <li class="contact__item">
        <svg class="contact__icon" viewBox="0 0 16 16" aria-hidden="true">
          <circle cx="8" cy="8" r="6.3" fill="none" stroke="var(--icon)" stroke-width="1.4"/>
          <path d="M1.7 8h12.6M8 1.7c-3 3.4-3 9.2 0 12.6M8 1.7c3 3.4 3 9.2 0 12.6" fill="none" stroke="var(--icon)" stroke-width="1.2"/>
        </svg>
        <span>www.qvmsolutions-demo.com.au</span>
      </li>
    </ul>
  </section>

  <section class="card card--back" aria-label="Business card back">
    <div class="back__art" role="img" aria-label="Faint dark gear pattern"></div>
    <div class="brand">
      <span class="brand__name">QVM</span>
      <span class="brand__mark" aria-hidden="true"></span>
    </div>
    <div class="services">
      <p class="services__intro">Capable of providing, but not limited to, across Australia:</p>
      <ul class="services__list">
        <li class="services__item">Contract Maintenance Planning.</li>
        <li class="services__item">Skilled Mobile Maintenance labour hire.</li>
        <li class="services__item">New machine build specifications.</li>
        <li class="services__item">Plant risk assessments and inspections.</li>
        <li class="services__item">Shut down and rebuild program planning.</li>
        <li class="services__item">Preventative maintenance tasks, including build of materials lists, creation and review.</li>
      </ul>
    </div>
  </section>
</main>
</body>
</html>
```